We need a business card design for a new soccer program based in Melbourne, Victoria, Australia.
Coaching kids from 2 through to 14 develop social, motor and soccer skills, in a fun and friendly non-competitive environment.
Our company colours are blue and orange as seen in the logo attached below. However, we are happy for the font to be any modern colour that looks professional.
Target Market(s)
Mums and dads
Industry/Entity Type
Business
Contact Information for Business Card
business name: Bright Kick Soccer
Marko Delvino Director- 0451 738 015
Luke Ferrano Director- 0419 856 371
Tomas Kovalenko Head Coach
email: marko@brightkicksoccer.com.au
website: www.brightkicksoccer.com.au
Coaching kids from 2-14
https://www.facebook.com/brightkicksoccer (facebook page not required unless it looks good without being clustered)
Look and feel

```html
<!DOCTYPE html>
<html lang="en">
<head>
<meta charset="utf-8">
<title>Bright Kick Soccer – Business Card</title>
<link rel="stylesheet" href="https://fonts.googleapis.com/css2?family=Open+Sans:wght@400;700;800&family=Lato:wght@400;700&display=swap">
<style>
  :root {
    --orange: #f28322;
    --blue: #3a3990;
    --ink-soft: #4b4a9a;
    --card: #ffffff;
    --stage: #d9d9d9;
    --rule: #6b6ab0;
  }
  * { box-sizing: border-box; margin: 0; padding: 0; }
  html, body {
    width: 1200px; height: 900px; overflow: hidden;
    background: var(--stage);
  }
  .sheet {
    width: 1200px; height: 900px;
    display: flex; flex-direction: column; align-items: center; justify-content: center;
    gap: 44px;
  }
  .card {
    position: relative;
    width: 640px; height: 388px;
    background: var(--card);
    border-radius: 26px;
    box-shadow: 0 6px 18px rgba(0,0,0,0.18);
    overflow: hidden;
  }

  /* Front */
  .card--front {
    display: flex; flex-direction: column; align-items: center; justify-content: center;
    gap: 34px;
  }
  .brand {
    display: flex; align-items: center; gap: 14px;
    font-family: "Open Sans", sans-serif;
    font-weight: 800;
    color: var(--blue);
    line-height: 1;
  }
  .brand__dot {
    width: 30px; height: 30px; border-radius: 50%;
    background: var(--orange);
    flex: none;
  }
  .card--front .brand { font-size: 46px; }
  .tagline {
    font-family: "Open Sans", sans-serif;
    font-weight: 700;
    font-size: 27px;
    letter-spacing: 3px;
    color: var(--orange);
  }
  .tagline__ages { color: var(--blue); }

  /* Back */
  .card--back .brand {
    position: absolute; left: 40px; top: 54px;
    font-size: 34px; gap: 12px;
  }
  .card--back .brand__dot { width: 24px; height: 24px; }
  .social {
    position: absolute; left: 40px; bottom: 56px;
    display: flex; align-items: center; gap: 12px;
    font-family: "Lato", sans-serif;
    font-size: 18px;
    color: var(--ink-soft);
  }
  .social__mark {
    width: 22px; height: 22px; border-radius: 3px;
    background: var(--blue);
    flex: none;
  }
  .contact {
    position: absolute; right: 40px; top: 128px;
    width: 300px;
    font-family: "Lato", sans-serif;
    color: var(--ink-soft);
  }
  .contact__name {
    font-size: 22px; letter-spacing: 2.5px;
    color: var(--orange);
    text-transform: uppercase;
    line-height: 1.05;
  }
  .contact__role {
    font-size: 13px; letter-spacing: 5px;
    color: var(--blue);
    text-transform: uppercase;
    padding-bottom: 6px;
    border-bottom: 1.5px dotted var(--rule);
  }
  .contact__list { list-style: none; padding: 8px 0 6px; border-bottom: 1.5px dotted var(--rule); }
  .contact__item {
    display: flex; align-items: center; gap: 10px;
    font-size: 16px; line-height: 1.5;
  }
  .contact__icon { width: 16px; height: 16px; flex: none; }
  .contact__address { font-size: 16px; padding-top: 6px; }
</style>
</head>
<body>
<main class="sheet">

  <section class="card card--front" aria-label="Card front">
    <div class="brand"><span class="brand__dot"></span>Bright Kick Soccer</div>
    <p class="tagline">Coaching kids from <span class="tagline__ages">2-14</span></p>
  </section>

  <section class="card card--back" aria-label="Card back">
    <div class="brand"><span class="brand__dot"></span>Bright Kick Soccer</div>

    <div class="social">
      <span class="social__mark"></span>
      <span>www.clubpage.net/brightkicksoccer</span>
    </div>

    <div class="contact">
      <p class="contact__name">Marko Delvino</p>
      <p class="contact__role">Director</p>
      <ul class="contact__list">
        <li class="contact__item">
          <svg class="contact__icon" viewBox="0 0 16 16" aria-hidden="true"><path d="M4 1.5l2.2 3-1.3 1.6a8 8 0 0 0 5 5l1.6-1.3 3 2.2-1.4 2.3C8 14.5 1.5 8 1.7 2.9z" fill="var(--orange)"/></svg>
          <span>: 0451 738 015</span>
        </li>
        <li class="contact__item">
          <svg class="contact__icon" viewBox="0 0 16 16" aria-hidden="true"><rect x="1" y="3.5" width="14" height="9" fill="none" stroke="var(--orange)" stroke-width="1.4"/><path d="M1 3.5l7 5 7-5" fill="none" stroke="var(--orange)" stroke-width="1.4"/></svg>
          <span>: marko@brightkicksoccer.com.au</span>
        </li>
        <li class="contact__item">
          <svg class="contact__icon" viewBox="0 0 16 16" aria-hidden="true"><g fill="none" stroke="var(--orange)" stroke-width="1.3"><circle cx="8" cy="8" r="6.5"/><ellipse cx="8" cy="8" rx="2.8" ry="6.5"/><path d="M1.5 8h13M2.5 4.8h11M2.5 11.2h11"/></g></svg>
          <span>: www.brightkicksoccer.com.au</span>
        </li>
      </ul>
      <p class="contact__address">Parkview #4 Address line</p>
    </div>
  </section>

</main>
</body>
</html>
```